Visitenkarten-Design für Boutique-Unternehmensberatung
Zielgruppe
Boutique Unternehmensberatung für die Chemische Industrie. Wir unterstützen Unternehmen, die Beziehung zu Ihren Händlern zu optimieren.
Vorläufige Website kernwerk-consult.de kann ggf weitere Einblicke geben. Hinweis: Diese Website wurde bisher noch nicht professionell erstellt.
Aufgabenstellung
Die Visitenkarte sollte vertrauenserweckend und seriös wirken. Zeitgleich aber auch modern.

```html
<!DOCTYPE html>
<html lang="de">
<head>
<meta charset="utf-8">
<title>Kernwerk Consult – Visitenkarte</title>
<link href="https://fonts.googleapis.com/css2?family=Montserrat:wght@400;500;700&display=swap" rel="stylesheet">
<style>
:root{
  --blue:#1f55b3;
  --blue-deep:#174496;
  --paper:#f1f0ec;
  --ink-soft:#3c6cc4;
  --stage:#e6e7ea;
  --photo:#c9a48c;
}
*{margin:0;padding:0;box-sizing:border-box}
html,body{width:1200px;height:918px;overflow:hidden;background:var(--stage);font-family:"Montserrat",sans-serif}
.sheet{position:relative;width:1200px;height:918px;display:flex;align-items:center;justify-content:center;gap:40px}
.card{position:relative;width:520px;height:336px;border-radius:6px;overflow:hidden;box-shadow:0 6px 20px rgba(0,0,0,.12)}
.card-back{background:var(--paper)}
.card-back .band{position:absolute;inset:0}
.brand-mini{position:absolute;left:28px;top:150px;display:flex;align-items:center;gap:8px;color:var(--ink-soft);font-weight:500;font-size:14px;line-height:1.1}
.brand-mini .dot{width:14px;height:14px;border-radius:50%;background:var(--ink-soft)}
.portrait{position:absolute;left:146px;top:68px;width:72px;height:72px;border-radius:50%;border:3px solid #fff;background:radial-gradient(circle at 50% 40%,#d9b9a2,var(--photo))}
.identity{position:absolute;left:200px;top:20px;color:#fff;white-space:nowrap}
.identity .name{font-weight:700;font-size:17px;letter-spacing:.3px}
.identity .role{font-weight:400;font-size:10.5px;margin-left:5px}
.identity .line{display:flex;align-items:center;gap:5px;font-size:10px;margin-top:8px}
.icon{width:12px;height:12px;flex:none}
.company{position:absolute;left:210px;top:196px;color:var(--ink-soft);font-size:10.5px;line-height:1.55;white-space:nowrap}
.company .rows{margin-top:8px}
.company .line{display:flex;align-items:center;gap:7px}
.card-front{background:radial-gradient(ellipse at 50% 50%,var(--blue) 55%,var(--blue-deep) 100%);display:flex;align-items:center;justify-content:center}
.brand{display:flex;align-items:center;gap:14px;color:var(--paper);font-weight:700;font-size:34px;letter-spacing:.5px}
.brand .dot{width:30px;height:30px;border-radius:50%;background:var(--paper)}
</style>
</head>
<body>
<main class="sheet">
  <section class="card card-back">
    <svg class="band" width="520" height="336" viewBox="0 0 520 336" aria-hidden="true">
      <path d="M0 0H520V205C430 196 320 170 230 120C160 80 80 48 0 40Z" fill="var(--blue)"/>
    </svg>
    <div class="brand-mini"><span class="dot"></span><span>Kernwerk<br>Consult</span></div>
    <div class="portrait" role="img" aria-label="Porträtfoto des Geschäftsführers"></div>
    <div class="identity">
      <div><span class="name">Jonas Albrecht</span><span class="role">• Geschäftsführer / CEO</span></div>
      <div class="line">
        <svg class="icon" viewBox="0 0 12 12"><circle cx="6" cy="6" r="6" fill="#fff"/><path d="M4 3l1 2-1 1c.5 1 1 1.5 2 2l1-1 2 1-.5 1.5C6 9.5 2.5 6 3 3.5z" fill="var(--blue)"/></svg>
        <span>+49 6100 / 12 34 56 78</span>
        <svg class="icon" viewBox="0 0 12 12" style="margin-left:10px"><circle cx="6" cy="6" r="6" fill="#fff"/><rect x="3" y="4" width="6" height="4.5" fill="none" stroke="var(--blue)"/><path d="M3 4l3 2.5L9 4" fill="none" stroke="var(--blue)"/></svg>
        <span>ja@kernwerk-consult.de</span>
      </div>
    </div>
    <div class="company">
      <div>Kernwerk Consult GmbH</div>
      <div>Lindenweg 12</div>
      <div>60311 Frankfurt</div>
      <div class="rows">
        <div class="line"><svg class="icon" viewBox="0 0 12 12"><circle cx="6" cy="6" r="6" fill="var(--ink-soft)"/><path d="M4 3l1 2-1 1c.5 1 1 1.5 2 2l1-1 2 1-.5 1.5C6 9.5 2.5 6 3 3.5z" fill="#fff"/></svg>+49 6100 / 12 34 56 78</div>
        <div class="line"><svg class="icon" viewBox="0 0 12 12"><circle cx="6" cy="6" r="6" fill="var(--ink-soft)"/><rect x="3" y="4" width="6" height="4.5" fill="none" stroke="#fff"/><path d="M3 4l3 2.5L9 4" fill="none" stroke="#fff"/></svg>ja@kernwerk-consult.de</div>
        <div class="line"><svg class="icon" viewBox="0 0 12 12"><circle cx="6" cy="6" r="6" fill="var(--ink-soft)"/><circle cx="6" cy="6" r="3.2" fill="none" stroke="#fff"/><path d="M2.8 6h6.4M6 2.8v6.4" stroke="#fff" stroke-width=".8"/></svg>www.kernwerk-consult.de</div>
      </div>
    </div>
  </section>
  <section class="card card-front">
    <div class="brand"><span class="dot"></span><span>Kernwerk Consult</span></div>
  </section>
</main>
</body>
</html>
```